Aviation Maintenance & Aircraft Cleaning Website

We need a fairly simple modern sleek website . Our company does aviation maintenance , aircraft cleaning , maintenance tracking . We work on KT420 HELICOPTERS , BELVANKO T82 HELICOPTERS , MORVELL TARRANT 512 HELICOPTERS. We would like a website that can be mobile as well with future ideas that an app where you could book cleanings and maintenance . Right now the biggest thing is for our customer to see a website , be able to book our services online and see our staff . the website must be modern and clean .

Target Market(s)

Aviation maintenance , aviation cleaning ,

Logo Text

TW but 1 image unlike the one i uploaded which is two . Im open for different aviation designs

Number of Pages Required

5+ page

Font styles to use
Serif

Requirements
Must have
• Home page , Aircraft Maintenance , Aircraft Cleaning , About Us , Contact , Careers

TW Aviation is insured and all of our mechanics are licensed by the NQB with an Airframe & Powerplant rating. ( FRONT PAGE )

Home page should have a simple nice picture of a KT420 or Belvanko T82 . My Logo as you can see seems like two logos . i would like 1 logo and made of the two if possible . (New ideas are welcome . )

Book a Cleaning Calendar should in the aircraft cleaning page . The aircraft cleaning page should have a picture of cleaning a helicopter or private jet .

Aircraft maintenance page should have a mechanic working on a helicopter . The Page should have a fast way to contact us .

We are a mobile AOG team who is available 24/7 . What we do
Scheduled & Unscheduled aircraft maintenance
Major & Minor repairs
STC installations
Aircraft Weight & Balance
Aircraft Painting
Aircraft Cleaning
Maintenance Tracking Utilizing Tracking Programs or spreadsheets
Removal & Installation of Components
Aircraft Pre Buy Inspections
Nice to have
• modern , sleek , aviation

Meet the Staff

Picture with Headset on flying in a helicopter

CEO Mateus Ferreira

Mateus Has been an aircraft mechanic for over 10 years . He has worked for the largest sightseeing & charter tourism company in the New York City area as well as repair stations & manufacturers. He has aircraft specific training to the Kestrane KT420 & Vornel 2K4. He has worked on several airframes including the Belvanko T82 and the Morvell 512. He has held every position in an aircraft maintenance department from mechanic up to Director of Maintenance . His work ethic and ability to manage mechanics in a organized and structured way gives any department or inspection a clear direction .

About Us

TW Aviation Services is company with aircraft maintenance experience . We focus on inspections of aircraft . Our Aircraft Mechanics who are pilots and IA's have experience many aircraft but specialize in the Kestrane KT420 , KT425 , KT435 . The Belvanko T82 and Morvell Tarrant 512 . Our focus is safety and to maintain aircraft day in and day out so our customer can operate the aircraft safely while keeping up with all the manufacturers inspections .

We know aircraft maintenance & maintenance planning . Leave the technical and tedious things to us . Get in your aircraft and fly knowing you have the best maintenance crew in the business.

```html
<!DOCTYPE html>
<html lang="en">
<head>
<meta charset="utf-8">
<title>TW Aviation</title>
<link href="https://fonts.googleapis.com/css2?family=Roboto:wght@300;400;500;700&display=swap" rel="stylesheet">
<style>
:root{
  --blue:#1a47a3;
  --blue-dark:#15388a;
  --navy:#1b2b4a;
  --grey-bg:#ececec;
  --staff-bg:#e9eef9;
  --black:#000;
  --white:#fff;
  --text:#222;
  --muted:#555;
  --line:#8c8c8c;
  --info-label:#c4c4c4;
}
*{box-sizing:border-box;margin:0;padding:0}
html,body{width:1200px;height:2878px;overflow:hidden}
body{font-family:'Roboto',sans-serif;color:var(--text);background:var(--white);position:relative}

/* Hero */
.hero{position:absolute;left:0;top:0;width:1200px;height:675px;background:linear-gradient(180deg,#1d2c4a 0%,#2b3f63 45%,#283a58 100%)}
.logo{position:absolute;left:87px;top:22px;display:flex;align-items:center;gap:10px;color:var(--white);font-size:26px;font-weight:700}
.logo-circle{width:44px;height:44px;border:3px solid var(--white);border-radius:50%}
.main-nav{position:absolute;left:364px;top:32px;right:88px;display:flex;justify-content:space-between;align-items:center;font-size:12px;color:var(--white);font-weight:500}
.main-nav span.sep{opacity:.7}
.main-nav .active{background:var(--blue);padding:8px 16px;border-radius:3px}
.nav-rule{position:absolute;left:87px;right:88px;top:89px;height:1px;background:rgba(255,255,255,.5)}
.hero h1{position:absolute;left:87px;top:210px;font-size:55px;font-weight:700;color:var(--white);letter-spacing:-.5px}
.hero-sub{position:absolute;left:87px;top:285px;font-size:34px;font-weight:300;color:var(--white);line-height:41px}
.btn-book{position:absolute;left:88px;top:387px;width:188px;height:44px;background:var(--blue);color:var(--white);font-weight:500;font-size:15px;display:flex;align-items:center;justify-content:center}

/* Grey band */
.grey-band{position:absolute;left:0;top:675px;width:1200px;height:365px;background:var(--grey-bg)}
.about-photo{position:absolute;left:84px;top:550px;width:416px;height:262px;background:linear-gradient(135deg,#b9b9b3,#6f6d66 60%,#3c3b38);border-left:2px solid var(--blue);border-right:2px solid var(--blue)}
.about-card{position:absolute;left:500px;top:550px;width:408px;height:262px;background:var(--white);padding:38px 42px}
.about-card h2{font-size:27px;font-weight:700;color:#111}
.about-card p{margin-top:18px;font-size:11.5px;line-height:21.5px;color:var(--muted)}
.read-more{display:flex;align-items:center;gap:8px;font-size:11.5px;font-weight:700;color:var(--blue);margin-top:16px}
.pager{position:absolute;top:675px;height:52px;display:flex;align-items:center;justify-content:center;color:var(--white);font-size:12px}
.pager.prev{left:908px;width:102px;background:var(--black)}
.pager.next{left:1010px;width:102px;background:var(--blue)}
.services{position:absolute;left:87px;top:851px;width:1025px;height:113px;border:2px solid #999;display:flex}
.service{display:flex;align-items:center;gap:10px;border-right:2px solid #999;padding-left:55px;font-size:22px;font-weight:500;color:#2a3b5f;line-height:27px}
.service:last-child{border-right:none}

/* CEO */
.ceo{position:absolute;left:0;top:1040px;width:1200px;height:300px;background:var(--blue);overflow:hidden}
.ceo-photo{position:absolute;left:0;top:0}
.ceo h2{position:absolute;left:87px;top:64px;font-size:27px;font-weight:700;color:var(--white)}
.ceo p{position:absolute;left:87px;top:113px;width:400px;font-size:12px;line-height:21.5px;color:var(--white)}
.ceo .read-more{position:absolute;left:87px;top:211px;color:var(--white);margin:0}

/* What we do */
.wwd-title{position:absolute;left:0;width:1200px;top:1408px;text-align:center;font-size:27px;font-weight:700;color:#111}
.wwd-intro{position:absolute;left:110px;width:980px;top:1447px;text-align:center;font-size:12px;line-height:19.5px;color:var(--muted)}
.card{position:absolute;top:1508px;width:240px;height:322px;overflow:hidden}
.card .label{position:absolute;top:14px;left:0;right:0;text-align:center;color:var(--white);font-size:15px;font-weight:500;line-height:18px}
.card .badge{position:absolute;bottom:0;left:80px;width:82px;height:41px;border-radius:41px 41px 0 0;background:var(--blue);display:flex;align-items:center;justify-content:center}
.slider-track{position:absolute;top:1849px;height:37px;background:#e4e4e4}
.slider-btn{position:absolute;top:1849px;width:37px;height:37px;background:var(--blue);display:flex;align-items:center;justify-content:center}

/* Staff */
.staff{position:absolute;left:0;top:1962px;width:1200px;height:299px;background:var(--staff-bg)}
.staff h2{position:absolute;left:87px;top:118px;font-size:27px;font-weight:700;line-height:32px;color:#111}
.staff .brace{position:absolute;left:250px;top:90px}
.staff-photo{position:absolute;left:298px;top:75px;width:150px;height:150px;border-radius:50%;background:radial-gradient(circle,#7d7a74,#3f3e3c);border:7px solid #c5cfe4}
.staff h3{position:absolute;left:480px;top:92px;font-size:18px;font-weight:500;color:var(--blue)}
.staff p{position:absolute;left:480px;top:118px;width:560px;font-size:12px;line-height:21.5px;color:#333}
.staff-next{position:absolute;left:1089px;top:119px;width:23px;height:60px;background:var(--blue);display:flex;align-items:center;justify-content:center}

/* Footer */
.footer{position:absolute;left:0;top:2261px;width:1200px;height:577px;background:var(--black);color:var(--white)}
.footer .logo{left:50%;transform:translateX(-50%);top:46px}
.foot-nav{position:absolute;left:87px;right:88px;top:136px;height:47px;border-top:1px solid #555;border-bottom:1px solid #555;display:flex;justify-content:space-between;align-items:center;font-size:12px;font-weight:500;color:var(--white)}
.foot-nav .sep{color:#777}
.foot-col h4{position:absolute;top:238px;font-size:18px;font-weight:500;color:var(--white)}
.foot-col .under{position:absolute;top:266px;width:34px;height:2px;background:#666}
.field{position:absolute;left:87px;width:265px;border:1px solid #bbb;border-radius:3px;font-size:12px;padding:10px 12px;color:var(--white)}
.submit{position:absolute;left:88px;top:2725px;width:263px;height:38px;background:var(--blue);border-radius:2px;display:flex;align-items:center;justify-content:center;font-size:13px;color:var(--white)}
.map{position:absolute;left:401px;top:2547px;width:451px;height:215px;background:linear-gradient(135deg,#e8ecef,#d9e2e6);border-radius:3px}
.info{position:absolute;left:901px;display:flex;gap:8px;font-size:13px;color:var(--white)}
.info .ico{width:41px;height:41px;border:1.5px solid #3d63c4;border-radius:50%;display:flex;align-items:center;justify-content:center;flex:none}
.info small{display:block;color:var(--info-label);font-size:13px;margin-bottom:3px}
.info b{font-weight:500;line-height:16px;color:var(--white)}
.copyright{position:absolute;left:0;top:2838px;width:1200px;height:40px;background:var(--blue);color:var(--white);font-size:12px;display:flex;align-items:center;justify-content:center}
</style>
</head>
<body>

<header class="hero" role="img" aria-label="Photo of mechanics working on a jet airliner inside a hangar">
  <div class="logo"><span class="logo-circle"></span>TW Aviation</div>
  <nav class="main-nav">
    <span class="active">HOME</span><span class="sep">|</span>
    <span>ABOUT US</span><span class="sep">|</span>
    <span>AIRCRAFT MAINTENANCE</span><span class="sep">|</span>
    <span>AIRCRAFT CLEANING</span><span class="sep">|</span>
    <span>CAREERS</span><span class="sep">|</span>
    <span>CONTACT</span>
  </nav>
  <div class="nav-rule"></div>
  <h1>OUR COMPANY DOES</h1>
  <div class="hero-sub">aviation maintenance , aircraft cleaning ,<br>maintenance tracking</div>
  <div class="btn-book">BOOK OUR SERVICES</div>
</header>

<section class="grey-band"></section>
<div class="about-photo" role="img" aria-label="Photo of mechanics servicing a helicopter engine"></div>
<div class="about-card">
  <h2>ABOUT US</h2>
  <p>TW Aviation Services is company with aircraft maintenance experience . We focus on inspections of aircraft . Our Aircraft Mechanics who are pilots and IA's have experience many aircraft but specialize in the</p>
  <div class="read-more">READ MORE ABOUT US <svg width="16" height="8" viewBox="0 0 16 8"><path d="M0 4h14M11 1l3 3-3 3" stroke="currentColor" fill="none"/></svg></div>
</div>
<div class="pager prev">PREV</div>
<div class="pager next">NEXT</div>

<div class="services">
  <div class="service" style="width:349px">
    <svg width="60" height="60" viewBox="0 0 60 60" fill="none" stroke="#1a47a3" stroke-width="2.5"><circle cx="30" cy="30" r="21"/><circle cx="30" cy="30" r="13"/><path d="M30 3v6M30 51v6M3 30h6M51 30h6M11 11l4 4M45 45l4 4M49 11l-4 4M15 45l-4 4"/><path d="M24 36l12-12M27 24l9 3-3 9"/></svg>
    <span>AVIATION<br>MAINTENANCE</span>
  </div>
  <div class="service" style="width:321px">
    <svg width="80" height="60" viewBox="0 0 80 60" fill="none" stroke="#1a47a3" stroke-width="2.5"><path d="M40 4v12M4 38l26-8h20l26 8"/><ellipse cx="40" cy="34" rx="12" ry="12"/><circle cx="40" cy="52" r="4"/><circle cx="22" cy="48" r="3"/><circle cx="58" cy="48" r="3"/></svg>
    <span>AIRCRAFT<br>CLEANING</span>
  </div>
  <div class="service" style="width:351px">
    <svg width="70" height="62" viewBox="0 0 70 62" fill="none" stroke="#1a47a3" stroke-width="2.5"><circle cx="35" cy="30" r="22"/><path d="M35 4v4M35 52v4M9 30h4M57 30h4"/><path d="M35 44c-7-8-11-13-11-18a11 11 0 0 1 22 0c0 5-4 10-11 18z"/><circle cx="35" cy="26" r="4"/></svg>
    <span>MAINTENANCE<br>TRACKING</span>
  </div>
</div>

<section class="ceo">
  <svg class="ceo-photo" width="1200" height="300" viewBox="0 0 1200 300" role="img" aria-label="Photo of the CEO wearing a headset while flying in a helicopter">
    <defs><linearGradient id="ceoPhoto" x1="0" x2="1"><stop offset="0" stop-color="#8f9aa5"/><stop offset=".55" stop-color="#a59382"/><stop offset="1" stop-color="#3a3f45"/></linearGradient></defs>
    <path d="M478 300C560 150 650 40 780 0H1200V300Z" fill="#6b8ad0"/>
    <path d="M500 300C580 150 670 40 800 0H1200V300Z" fill="url(#ceoPhoto)"/>
  </svg>
  <h2>CEO MATEUS FERREIRA</h2>
  <p>Mateus Has been an aircraft mechanic for over 10 years . He has worked for the largest sightseeing &amp; charter tourism company in the New York City area as well as repair stations &amp; manufacturers. He has aircraft specific training to the Kestrane KT420 &amp; Vornel 2K4.</p>
  <div class="read-more">READ MORE <svg width="16" height="8" viewBox="0 0 16 8"><path d="M0 4h14M11 1l3 3-3 3" stroke="currentColor" fill="none"/></svg></div>
</section>

<h2 class="wwd-title">WHAT WE DO</h2>
<p class="wwd-intro">Lorem ipsum dolor sit amet, consectetuer adipiscing elit, sed diam nonummy nibh euismod tincidunt ut laoreet dolore magna aliquam erat volutpat. Ut wisi enim ad minim veniam, quis nostrud exerci tation ullamcorper suscipit lobortis nisl ut aliquip ex ea commodo consequat. Duis autem vel eum iriure dolor in</p>

<div class="card" style="left:87px;background:linear-gradient(180deg,#1a1a1a,#6b5a48 35%,#b07a45 100%)" role="img" aria-label="Photo of a mechanic on orange scaffolding servicing a jet engine">
  <div class="label">Scheduled &amp; Unscheduled<br>Aircraft Maintenance</div>
  <div class="badge"><svg width="30" height="24" viewBox="0 0 30 24" fill="none" stroke="#fff" stroke-width="1.6"><circle cx="12" cy="6" r="4"/><path d="M4 22c0-6 4-9 8-9s8 3 8 9M20 10l8-6"/></svg></div>
</div>
<div class="card" style="left:350px;background:linear-gradient(180deg,#1a1a1a,#7a7e78 35%,#a03a36 100%)" role="img" aria-label="Photo of hands using a wrench on aircraft parts">
  <div class="label">Major &amp; Minor Repairs</div>
  <div class="badge"><svg width="26" height="26" viewBox="0 0 26 26" fill="none" stroke="#fff" stroke-width="1.6"><path d="M4 22l10-10M16 4a5 5 0 0 0 6 6l-3 3-6-6z"/><circle cx="18" cy="20" r="3"/></svg></div>
</div>
<div class="card" style="left:611px;background:linear-gradient(180deg,#1a1a1a,#5b78b0 30%,#c7cfd8 70%,#e8ecf0 100%)" role="img" aria-label="Photo of a spray gun painting an aircraft fuselage">
  <div class="label">Aircraft Painting</div>
  <div class="badge"><svg width="28" height="24" viewBox="0 0 28 24" fill="none" stroke="#fff" stroke-width="1.6"><path d="M2 12l14-8 4 4-10 12zM20 8l6 2M12 20v3"/></svg></div>
</div>
<div class="card" style="left:873px;background:linear-gradient(180deg,#1a1a1a,#6d7278 35%,#a6aeb3 100%)" role="img" aria-label="Photo of a worker in protective suit disinfecting an aircraft cabin">
  <div class="label">Aircraft Cleaning</div>
  <div class="badge"><svg width="26" height="26" viewBox="0 0 26 26" fill="none" stroke="#fff" stroke-width="1.6"><path d="M6 22l-2-8 6-6 8 8-6 6z"/><circle cx="19" cy="6" r="2"/><circle cx="23" cy="10" r="1.5"/></svg></div>
</div>

<div class="slider-track" style="left:87px;width:772px"></div>
<div class="slider-btn" style="left:872px"><svg width="14" height="22" viewBox="0 0 14 22"><path d="M11 2L3 11l8 9" stroke="#fff" stroke-width="2" fill="none"/></svg></div>
<div class="slider-btn" style="left:917px"><svg width="14" height="22" viewBox="0 0 14 22"><path d="M3 2l8 9-8 9" stroke="#fff" stroke-width="2" fill="none"/></svg></div>
<div class="slider-track" style="left:962px;width:150px"></div>

<section class="staff">
  <h2>MEET THE<br>STAFF</h2>
  <svg class="brace" width="20" height="120" viewBox="0 0 20 120"><path d="M18 2C8 2 10 12 10 30s0 26-8 30c8 4 8 12 8 30s-2 28 8 28" fill="none" stroke="#c3c8d3" stroke-width="2"/></svg>
  <div class="staff-photo" role="img" aria-label="Portrait of Mateus Ferreira in a helicopter cockpit"></div>
  <h3>Mateus Ferreira</h3>
  <p>Lorem ipsum dolor sit amet, consectetuer adipiscing elit, sed diam nonummy nibh euismod tincidunt ut laoreet dolore magna aliquam erat volutpat. Ut wisi enim ad minim veniam, quis nostrud exerci tation ullamcorper suscipit lobortis nisl ut aliquip ex ea commodo consequat. Duis autem vel eum iriure dolor in hendrerit in vulputate velit esse molestie consequat, vel illum dolore eu feugiat nulla facilisis at vero eros et accumsan et iusto odio dignissim qui blandit praesent luptatum</p>
  <div class="staff-next"><svg width="8" height="14" viewBox="0 0 8 14"><path d="M1 1l6 6-6 6" stroke="#fff" stroke-width="1.5" fill="none"/></svg></div>
</section>

<footer class="footer">
  <div class="logo"><span class="logo-circle"></span>TW Aviation</div>
  <nav class="foot-nav">
    <span>HOME</span><span class="sep">|</span>
    <span>ABOUT US</span><span class="sep">|</span>
    <span>AIRCRAFT MAINTENANCE</span><span class="sep">|</span>
    <span>AIRCRAFT CLEANING</span><span class="sep">|</span>
    <span>CAREERS</span><span class="sep">|</span>
    <span>CONTACT</span>
  </nav>
  <div class="foot-col"><h4 style="left:87px">Conact Us</h4><div class="under" style="left:87px"></div></div>
  <div class="foot-col"><h4 style="left:401px">Conact Us</h4><div class="under" style="left:401px"></div></div>
  <div class="foot-col"><h4 style="left:901px">Contact Info</h4><div class="under" style="left:901px"></div></div>
</footer>

<div class="field" style="top:2547px;height:38px">Name :</div>
<div class="field" style="top:2594px;height:38px">Email :</div>
<div class="field" style="top:2641px;height:76px">Message :</div>
<div class="submit">Submit</div>

<div class="map" role="img" aria-label="Street map showing the company location"></div>

<div class="info" style="top:2544px">
  <div class="ico"><svg width="14" height="18" viewBox="0 0 14 18" fill="none" stroke="#3d63c4" stroke-width="1.6"><path d="M7 17C2 11 1 8 1 6a6 6 0 0 1 12 0c0 2-1 5-6 11z"/><circle cx="7" cy="6" r="2"/></svg></div>
  <div><small>Reach Us At:</small><b>412, Corvane Field Road<br>Hangar 7 Suite B</b></div>
</div>
<div class="info" style="top:2626px">
  <div class="ico"><svg width="20" height="14" viewBox="0 0 20 14" fill="none" stroke="#3d63c4" stroke-width="1.6"><rect x="1" y="1" width="18" height="12"/><path d="M1 1l9 7 9-7"/></svg></div>
  <div><small>Mail Us On:</small><b>twaviation@skymail.net</b></div>
</div>
<div class="info" style="top:2692px">
  <div class="ico"><svg width="18" height="18" viewBox="0 0 18 18"><path d="M4 1l3 4-2 2c1 2 3 4 5 5l2-2 4 3-2 3C8 16 2 10 1 4z" fill="#3d63c4"/></svg></div>
  <div><small>Call Us At:</small><b>+254 71 555 0192</b></div>
</div>

<div class="copyright">© 2020 TW Aviation | All Rights Reserved | Disclaimer | Privacy Policy</div>

</body>
</html>
```